Scotch Whisky Label design

To create a unique Label for private bottling of rare single malt island whisky. Distilled in 1997 the whisky is 23 years and from the Island Of Arran. Design should encompass front label+ technical information (volume /drink waring /Alcohol % etc - all to be supplied) for the back lablel. Label should be CMYK only for digital printing. Label can include the island name but only as secondary information as thre brand Brackvane Malt Whisky is protected. Size of front label = approx 80mm x 120mm(portrait).

Design should be simple and effective, but to show quality and uniqueness of whisky

reference web link for ideas

https://www.peatcaskbidhall.example/auctions/148_the-52nd-sale/?page=12&area=

images show other similar items

images also show options for bottle style

Target Market(s)

Private buyers of rare whisky

Requirements
Must have
• Age of whisky (23 years)
• Single Island Arran Malt (in sub text)
Nice to have
• Traditonal illustration, reference of island geography
Should not have
• metalics,

```html
<!DOCTYPE html>
<html lang="en">
<head>
<meta charset="utf-8">
<title>Single Malt Island Whisky – Front Label</title>
<link rel="stylesheet" href="https://fonts.googleapis.com/css2?family=Rye&family=Old+Standard+TT:ital,wght@0,700;1,400&family=Pinyon+Script&family=Oswald:wght@500&display=swap">
<style>
  :root {
    --page: #f3f3f1;
    --label-green: #353a33;
    --map-tone: #3f453c;
    --gold: #c4992f;
    --cream: #fbf8f0;
  }
  html, body {
    margin: 0;
    padding: 0;
    width: 1200px;
    height: 1035px;
    overflow: hidden;
    background: var(--page);
  }
  .front-label {
    position: absolute;
    left: 256px;
    top: 37px;
    width: 688px;
    height: 960px;
    display: block;
  }
  .label-ground { fill: var(--label-green); }
  .frame-line { fill: none; stroke: var(--gold); stroke-width: 1.5; }
  .gold-rule { fill: none; stroke: var(--gold); stroke-width: 2; }
  .arch-caption {
    font-family: "Old Standard TT", Georgia, serif;
    font-weight: 700;
    fill: var(--cream);
    letter-spacing: 2px;
  }
  .title-word {
    font-family: "Rye", Georgia, serif;
    font-size: 128px;
    fill: var(--cream);
  }
  .title-shadow { fill: var(--gold); }
  .spaced-caption {
    font-family: "Old Standard TT", Georgia, serif;
    font-weight: 700;
    fill: var(--cream);
    letter-spacing: 6px;
  }
  .island-script {
    font-family: "Pinyon Script", cursive;
    font-size: 80px;
    fill: var(--gold);
  }
  .island-word {
    font-family: "Oswald", "Arial Narrow", sans-serif;
    font-weight: 500;
    font-size: 52px;
    fill: var(--cream);
  }
  .age-number {
    font-family: "Old Standard TT", Georgia, serif;
    font-style: italic;
    font-size: 58px;
    fill: var(--cream);
  }
  .age-ring { fill: none; stroke: var(--gold); }
</style>
</head>
<body>
<svg class="front-label" viewBox="0 0 688 960" xmlns="http://www.w3.org/2000/svg">
  <defs>
    <radialGradient id="mapTone" cx="50%" cy="50%" r="50%">
      <stop offset="0%" stop-color="#454b41"/>
      <stop offset="100%" stop-color="#353a33"/>
    </radialGradient>
    <path id="topArch" d="M150,222 Q344,88 538,222"/>
    <path id="bottomArch" d="M146,850 Q344,966 542,850"/>
  </defs>

  <rect class="label-ground" x="0" y="0" width="688" height="960"/>

  <g class="label-frame">
    <rect class="frame-line" x="14" y="14" width="660" height="932"/>
    <rect class="frame-line" x="22" y="22" width="644" height="916"/>
  </g>

  <ellipse class="island-map" role="img" aria-label="Engraved map of the island of Arran"
           cx="344" cy="470" rx="150" ry="400" fill="url(#mapTone)"/>

  <g class="heading-arch">
    <text class="arch-caption" font-size="34">
      <textPath href="#topArch" startOffset="50%" text-anchor="middle">SINGLE MALT ISLAND</textPath>
    </text>
    <path class="gold-rule" d="M98,240 Q344,132 590,240"/>
  </g>

  <g class="title">
    <text class="title-word title-shadow" x="347" y="407" text-anchor="middle" textLength="446" lengthAdjust="spacingAndGlyphs">WHISKY</text>
    <text class="title-word" x="344" y="402" text-anchor="middle" textLength="446" lengthAdjust="spacingAndGlyphs">WHISKY</text>
  </g>

  <text class="spaced-caption" x="344" y="478" font-size="26" text-anchor="middle">FROM</text>

  <g class="origin">
    <text class="island-script" x="318" y="566" text-anchor="middle">Arran</text>
    <text class="island-word" x="434" y="614" text-anchor="middle" textLength="168" lengthAdjust="spacingAndGlyphs">ISLAND</text>
  </g>

  <g class="age-statement">
    <text class="spaced-caption" x="262" y="775" font-size="32" text-anchor="end" letter-spacing="4">AGED</text>
    <circle class="age-ring" cx="344" cy="760" r="57" stroke-width="2.5"/>
    <circle class="age-ring" cx="344" cy="760" r="50" stroke-width="1.2"/>
    <text class="age-number" x="344" y="779" text-anchor="middle">23</text>
    <text class="spaced-caption" x="424" y="775" font-size="32" letter-spacing="4">YEARS</text>
    <line class="gold-rule" x1="118" y1="796" x2="570" y2="796"/>
    <line class="gold-rule" x1="130" y1="808" x2="558" y2="808" stroke-width="1.2"/>
  </g>

  <g class="distilled-arch">
    <path class="gold-rule" d="M96,806 Q344,912 592,806"/>
    <text class="arch-caption" font-size="36" letter-spacing="4">
      <textPath href="#bottomArch" startOffset="50%" text-anchor="middle">DISTILLED IN 1997</textPath>
    </text>
  </g>
</svg>
</body>
</html>
```